Business Card Design Project - bel soravin group

dear Sirs

we need business card design for our group ( BEL Soravin Group ) , i have got the Logo design of our group from pixel harbor in previous , so all need details relating to our group i think available with you, as well as the the chosen logo design

we hope to provide us with business card logo that to be appropaite and satisfactory to us .

thanks

note : logo design of our group is attached .
Updates

Reason: please extend the deadline of my project for additional 15 days because i didn't received appropriate design for our gruop yet . kindly beaware that i have received 77 design till now , supossed to send me 200-250 design at least . thanks

Target Market(s)

contents
-

name : Korvan EL Mistrani

position : Operation Manager

Industry/Entity Type

Business

Requirements
Must have

• person name

group logo
Nice to have
• logo color matching with back background

```html
<!DOCTYPE html>
<html lang="en">
<head>
<meta charset="utf-8">
<title>BEL Soravin Group – Business Card</title>
<link rel="stylesheet" href="https://fonts.googleapis.com/css2?family=Ubuntu+Condensed&display=swap">
<style>
  :root {
    --page-bg: #e6e8eb;
    --card-white: #f1f1f2;
    --card-blue: #0a5aa3;
    --ink-dark: #2a2a2c;
    --ink-blue: #1a5fa8;
    --ink-white: #ffffff;
    --ink-soft-blue: #6ea6dc;
  }
  * { margin: 0; padding: 0; box-sizing: border-box; }
  html, body {
    width: 1067px;
    height: 1200px;
    overflow: hidden;
    background: var(--page-bg);
    font-family: "Ubuntu Condensed", "Arial Narrow", sans-serif;
  }
  .sheet {
    width: 1067px;
    height: 1200px;
    display: flex;
    flex-direction: column;
    align-items: center;
    justify-content: center;
    gap: 80px;
  }
  .card {
    position: relative;
    width: 840px;
    height: 480px;
    overflow: hidden;
    background: var(--card-white);
    box-shadow: 0 6px 18px rgba(0, 0, 0, 0.18);
  }
  .card__band {
    position: absolute;
    left: 0;
    right: 0;
    bottom: 0;
    background: var(--card-blue);
  }
  .card--front .card__band { top: 262px; }
  .card--back .card__band { top: 176px; }

  .holder {
    position: absolute;
    left: 48px;
    top: 118px;
  }
  .holder__name {
    font-size: 42px;
    color: var(--ink-dark);
    font-weight: 400;
    line-height: 1;
  }
  .holder__role {
    margin-top: 14px;
    font-size: 21px;
    color: var(--ink-blue);
  }

  .contact {
    position: absolute;
    left: 52px;
    top: 312px;
    list-style: none;
    font-size: 24px;
    line-height: 29px;
    color: var(--ink-white);
  }
  .contact__item--web { color: var(--ink-soft-blue); }

  .brand {
    position: absolute;
    display: flex;
    align-items: center;
    color: var(--ink-white);
    white-space: nowrap;
  }
  .brand__mark {
    flex: none;
    border: 4px solid var(--ink-white);
  }
  .card--front .brand {
    right: 34px;
    top: 282px;
    gap: 14px;
    font-size: 44px;
  }
  .card--front .brand__mark { width: 38px; height: 38px; }
  .card--back .brand {
    left: 0;
    right: 0;
    top: 270px;
    justify-content: center;
    gap: 20px;
    font-size: 64px;
  }
  .card--back .brand__mark { width: 54px; height: 54px; }
</style>
</head>
<body>
<main class="sheet">
  <section class="card card--front" aria-label="Business card front">
    <div class="card__band"></div>
    <div class="holder">
      <h1 class="holder__name">Korvan EL Mistrani</h1>
      <p class="holder__role">Operation Manager</p>
    </div>
    <div class="brand">
      <span class="brand__mark"></span>
      <span class="brand__name">BEL Soravin Group</span>
    </div>
    <ul class="contact">
      <li class="contact__item">Phone: 0123 456 789</li>
      <li class="contact__item">Fax: 0123 456 789</li>
      <li class="contact__item contact__item--web">info@yourdomain.com</li>
      <li class="contact__item contact__item--web">www.yourdomain.com</li>
      <li class="contact__item">P.O. Box: City name, etc.</li>
    </ul>
  </section>

  <section class="card card--back" aria-label="Business card back">
    <div class="card__band"></div>
    <div class="brand">
      <span class="brand__mark"></span>
      <span class="brand__name">BEL Soravin Group</span>
    </div>
  </section>
</main>
</body>
</html>
```